Präsentationsvorlagen für IT-Systemhaus
Zielgruppe
Wir sind ein IT-Systemhaus, das Beratung und Dienstleistungen für kleine und mittelständische Unternehmen im gesamten deutschsprachigen Raum anbietet. Wir möchten uns gerne eine neue Präsentationsvorlage für PowerPoint erstellen lassen, welche sowohl für Unternehmenspräsentationen, als auch für Kundenpräsentationen im Projektumfeld gut verwendet werden kann.
Aufgabenstellung
Das Design sollte im 16:9 Format angelegt werden. Als Schriftart verwenden Sie bitte OpenSans und ggf. für die Überschriften Armata. Ansonsten sind Sie in der Gestaltung frei.
Vielen Dank für Ihre Mühe!

```html
<!DOCTYPE html>
<html lang="de">
<head>
<meta charset="utf-8">
<title>Präsentationsvorlage – Titelfolie</title>
<link rel="stylesheet" href="https://fonts.googleapis.com/css2?family=Armata&family=Open+Sans:wght@400&display=swap">
<style>
  :root {
    --brand-red: #a52f2e;
    --brand-grey: #6d6e71;
    --paper: #ffffff;
    --backdrop: #ffffff;
  }
  * { margin: 0; padding: 0; box-sizing: border-box; }
  html, body {
    width: 1200px;
    height: 670px;
    overflow: hidden;
    background: var(--backdrop);
  }
  .stage {
    position: relative;
    width: 1200px;
    height: 670px;
    overflow: hidden;
  }
  .stage__band {
    position: absolute;
    left: 0;
    top: 461px;
    width: 1200px;
    height: 209px;
    background: var(--brand-red);
  }
  .slide {
    position: absolute;
    left: 86px;
    top: 46px;
    width: 1032px;
    height: 580px;
    background: var(--paper);
    box-shadow: 0 6px 22px rgba(0, 0, 0, 0.28);
    overflow: hidden;
  }
  .slide__sidebar {
    position: absolute;
    left: 0;
    top: 0;
    width: 144px;
    height: 100%;
    background: var(--brand-grey);
  }
  .brand {
    position: absolute;
    right: 60px;
    top: 60px;
    display: flex;
    align-items: center;
    gap: 10px;
  }
  .brand__square {
    width: 30px;
    height: 30px;
    background: var(--brand-red);
  }
  .brand__name {
    font-family: "Armata", sans-serif;
    font-size: 34px;
    line-height: 1;
    color: var(--brand-grey);
  }
  .slide__title {
    position: absolute;
    left: 226px;
    top: 247px;
    font-family: "Armata", sans-serif;
    font-weight: 400;
    font-size: 86px;
    line-height: 1.1;
    letter-spacing: 1px;
    color: var(--brand-grey);
    white-space: nowrap;
  }
  .slide__lead {
    position: absolute;
    left: 226px;
    top: 372px;
    width: 620px;
    font-family: "Open Sans", sans-serif;
    font-size: 16.5px;
    line-height: 19.6px;
    color: var(--brand-grey);
  }
</style>
</head>
<body>
  <main class="stage">
    <div class="stage__band"></div>
    <section class="slide">
      <div class="slide__sidebar"></div>
      <div class="brand">
        <span class="brand__square"></span>
        <span class="brand__name">Nordwerk</span>
      </div>
      <h1 class="slide__title">Überschrift</h1>
      <p class="slide__lead">Lorem ipsum dolor sit amet, consectetuer adipiscing elit, sed diam nonummy nibh euismod tincidunt ut laoreet dolore magna aliquam erat volutpat. Ut wisi</p>
    </section>
  </main>
</body>
</html>
```